Global Expert Network Firm needs business card design

We need business card design for a new company based in Seoul, South Korea called 'Corwell Insight Partners'. We recruit industry experts covering all countries and connect our client and recruited expert by phone, face-to-face meetings and etc. We are a global expert network firm that is focused on delivering high-quality experts to our clients throughout the world. Our clients include multinational corporations, global consulting firms, private equity firms, venture capital firms, asset management companies.
We have made new logo and please find attachment.(Please use new logo)
Target Market(s)
Global Consulting Firms, Investment Firms, Private Equity Firms, Venture Capital Firms.
Industry/Entity Type
Recruitment
Contact Information for Business Card
We need two Languages (English and Korean Version).
The front is Korean and the back is English version.
[The back] [English]
Company Name: Corwell Insight Partners, Inc.
CEO Name: Daniel Park
Address: #507, Hanbit Bldg, 82 Maebongsan-ro, Dobong-gu, Seoul, 01327, Korea
Tel. +82 2 718 4052
Fax. +82 2 864 1097
Mobile. +82 10 7264 8815
Email: daniel@corwellip.com
Web: www.corwellip.com
[The front] [Korean] => Described in same order as English version.
회사명: 코웰인사이트파트너스(주)
대표이사: 박도현
주소: 서울시 도봉구 매봉산로 82 한빛빌딩 507호
Tel. 02 718 4052
Fax. 02 864 1097
Mobile. 010 7264 8815
Web: www.corwellip.com
Look and feel
Each slider illustrates characteristics of the customer's brand and the style your logo design should communicate.

```html
<!DOCTYPE html>
<html lang="en">
<head>
<meta charset="utf-8">
<title>Corwell Insight Partners — Business Cards</title>
<link rel="stylesheet" href="https://fonts.googleapis.com/css2?family=Nanum+Myeongjo:wght@400;700&family=Poppins:wght@300;400;600&display=swap">
<style>
  :root {
    --backdrop: #dcdcdc;
    --card-navy: #1b2150;
    --ink: #ffffff;
    --rule: rgba(255,255,255,0.8);
  }
  * { box-sizing: border-box; margin: 0; padding: 0; }
  html, body { width: 1200px; height: 1200px; overflow: hidden; }
  body {
    background: var(--backdrop);
    display: flex; align-items: center; justify-content: center; gap: 100px;
    font-family: "Poppins", sans-serif; color: var(--ink);
  }
  .card {
    position: relative; width: 400px; height: 720px;
    background: var(--card-navy);
    box-shadow: 0 6px 18px rgba(0,0,0,0.18);
  }
  .holder { position: absolute; right: 36px; top: 50px; width: 220px; }
  .holder-name {
    font-weight: 600; font-size: 27px; line-height: 1.2; text-align: right;
    padding-bottom: 4px; border-bottom: 1px solid var(--rule);
  }
  .holder-title { font-weight: 300; font-size: 12px; margin-top: 4px; letter-spacing: 0.5px; }

  .company {
    position: absolute; left: 56px; top: 258px; width: 240px;
    display: flex; align-items: flex-start; gap: 12px;
  }
  .company-mark { flex: none; width: 14px; height: 14px; margin-top: 8px; background: var(--ink); }
  .company-name { font-weight: 400; font-size: 24px; line-height: 1.3; color: var(--ink); }

  .contacts { position: absolute; left: 118px; top: 392px; width: 250px; }
  .contact-row { display: flex; }
  .contact-label {
    width: 30px; writing-mode: vertical-rl; font-size: 11px; font-weight: 400;
    letter-spacing: 1.5px; text-transform: uppercase; padding-top: 2px;
  }
  .contact-value {
    flex: 1; padding-left: 12px; border-left: 1px solid var(--rule);
    font-weight: 300; font-size: 13.5px; line-height: 1.45;
  }
  .row-address { height: 112px; }
  .row-tel, .row-fax { height: 46px; }
  .row-mobile { height: 68px; }

  .online {
    position: absolute; left: 168px; top: 660px; width: 200px;
    border-top: 1px solid var(--rule); padding-top: 4px;
    font-weight: 300; font-size: 14px; line-height: 1.4;
  }

  .card-ko .holder-name { font-family: "Nanum Myeongjo", serif; font-weight: 400; font-size: 34px; letter-spacing: 3px; }
  .card-ko .holder-title { font-family: "Nanum Myeongjo", serif; text-align: right; font-size: 14px; letter-spacing: 2px; }
  .card-ko .company-name { font-family: "Nanum Myeongjo", serif; font-weight: 400; font-size: 24px; line-height: 1.4; word-break: keep-all; }
  .card-ko .contact-label.ko { font-family: "Nanum Myeongjo", serif; font-size: 12px; letter-spacing: 6px; }
  .card-ko .address-ko { font-family: "Nanum Myeongjo", serif; font-size: 13.5px; line-height: 1.55; }
</style>
</head>
<body>
  <section class="card card-en" aria-label="English side">
    <div class="holder">
      <p class="holder-name">Daniel Park</p>
      <p class="holder-title">CEO</p>
    </div>
    <div class="company">
      <span class="company-mark" aria-hidden="true"></span>
      <p class="company-name">Corwell Insight Partners, Inc.</p>
    </div>
    <div class="contacts">
      <div class="contact-row row-address">
        <p class="contact-label">Address</p>
        <p class="contact-value">#507, Hanbit Bldg,<br>82 Maebongsan-ro,<br>Dobong-gu, Seoul, 01327,<br>Korea.</p>
      </div>
      <div class="contact-row row-tel">
        <p class="contact-label">Tel.</p>
        <p class="contact-value">+82 2 718 4052</p>
      </div>
      <div class="contact-row row-fax">
        <p class="contact-label">Fax.</p>
        <p class="contact-value">+82 2 864 1097</p>
      </div>
      <div class="contact-row row-mobile">
        <p class="contact-label">Mobile.</p>
        <p class="contact-value">+82 10 7264 8815</p>
      </div>
    </div>
    <div class="online">
      <p>daniel@corwellip.com</p>
      <p>www.corwellip.com</p>
    </div>
  </section>

  <section class="card card-ko" lang="ko" aria-label="Korean side">
    <div class="holder">
      <p class="holder-name">박도현</p>
      <p class="holder-title">대표이사</p>
    </div>
    <div class="company">
      <span class="company-mark" aria-hidden="true"></span>
      <p class="company-name">코웰인사이트<br>파트너스(주)</p>
    </div>
    <div class="contacts">
      <div class="contact-row row-address">
        <p class="contact-label ko">주소</p>
        <p class="contact-value address-ko">서울시 도봉구 매봉산로 82<br>한빛빌딩 507호</p>
      </div>
      <div class="contact-row row-tel">
        <p class="contact-label">Tel.</p>
        <p class="contact-value">+82 2 718 4052</p>
      </div>
      <div class="contact-row row-fax">
        <p class="contact-label">Fax.</p>
        <p class="contact-value">+82 2 864 1097</p>
      </div>
      <div class="contact-row row-mobile">
        <p class="contact-label">Mobile.</p>
        <p class="contact-value">+82 10 7264 8815</p>
      </div>
    </div>
    <div class="online">
      <p>daniel@corwellip.com</p>
      <p>www.corwellip.com</p>
    </div>
  </section>
</body>
</html>
```